High-end residential home builder needs a business card design

We need a new business card design for a small residential construction company based in Boise, Idaho. We specialize in building custom high-end homes and remodels, with a focus on great design and craftsmanship.

We would like to use our current logo, but open to new color suggestions.
Just looking for a clean, sharp, modern design that looks high-end.

Target Market(s)

Upscale clientele

Industry/Entity Type

Contractor

Contact Information for Business Card

Company: Stonefield Custom Builders
Name: Marcus Tilley
Phone number: 208 367 4120
Email: MarcusTilleySCB@mailbox-example.com
Website: Stonefieldcustombuilders-example.com

Font styles to use
Serif
Sans Serif

Requirements
Must have
• Company Logo
Company name
My name
My phone number
My email
Company website
Nice to have
• I have attached a few photos of cards that I really like.

```html
<!DOCTYPE html>
<html lang="en">
<head>
<meta charset="utf-8">
<title>Stonefield Custom Builders – Business Card</title>
<link rel="stylesheet" href="https://fonts.googleapis.com/css2?family=Raleway:wght@500;600&family=Lato:wght@400&display=swap">
<style>
  :root {
    --backdrop: #858585;
    --paper: #ffffff;
    --walnut: #321c0b;
    --amber: #e08a1e;
    --ink: #2a1a0e;
  }
  * { box-sizing: border-box; margin: 0; padding: 0; }
  html, body { width: 1200px; height: 1200px; overflow: hidden; }
  body { background: var(--backdrop); position: relative; font-family: "Lato", sans-serif; }

  .card { position: absolute; left: 254px; width: 692px; height: 395px; }
  .card-front { top: 160px; background: var(--paper); }
  .card-back { top: 644px; background: var(--walnut); }

  .brand { position: absolute; display: flex; align-items: center; }
  .brand-mark { width: 42px; height: 42px; border: 2px solid var(--amber); flex: none; }
  .brand-name {
    font-family: "Raleway", sans-serif; font-weight: 600;
    font-size: 15px; letter-spacing: 0.32em; line-height: 1.6; text-transform: uppercase;
  }
  .card-front .brand { left: 46px; top: 170px; gap: 18px; }
  .card-front .brand-name { color: var(--ink); }

  .divider { position: absolute; left: 355px; top: 138px; width: 2px; height: 119px; background: var(--amber); }

  .contact { position: absolute; left: 383px; top: 132px; color: var(--ink); }
  .contact-name {
    font-family: "Raleway", sans-serif; font-weight: 500;
    font-size: 28px; color: var(--amber); line-height: 1.1; letter-spacing: 0.01em;
  }
  .contact-role { font-size: 16px; margin-top: 3px; }
  .contact-list { list-style: none; margin-top: 14px; }
  .contact-list li { display: flex; align-items: center; gap: 6px; font-size: 14.5px; line-height: 22px; }
  .contact-list svg { width: 11px; height: 11px; flex: none; }

  .card-back .brand { left: 0; right: 0; top: 140px; flex-direction: column; gap: 22px; text-align: center; }
  .card-back .brand-mark { width: 72px; height: 72px; }
  .card-back .brand-name { color: var(--paper); font-size: 20px; }
</style>
</head>
<body>
  <section class="card card-front">
    <div class="brand">
      <span class="brand-mark"></span>
      <p class="brand-name">Stonefield<br>Custom Builders</p>
    </div>
    <span class="divider"></span>
    <div class="contact">
      <h1 class="contact-name">MARCUS TILLEY</h1>
      <p class="contact-role">Director</p>
      <ul class="contact-list">
        <li>
          <svg viewBox="0 0 12 12"><path d="M3 1 L5 3.2 L4 4.5 Q5 7 7.5 8 L8.8 7 L11 9 L9.6 11 Q3.5 10.5 1 3 Z" fill="var(--amber)"/></svg>
          208 367 4120
        </li>
        <li>
          <svg viewBox="0 0 12 12"><rect x="1" y="2.5" width="10" height="7" fill="none" stroke="var(--amber)" stroke-width="1.2"/><path d="M1 2.5 L6 6.5 L11 2.5" fill="none" stroke="var(--amber)" stroke-width="1.2"/></svg>
          MarcusTilleySCB@mailbox-example.com
        </li>
        <li>
          <svg viewBox="0 0 12 12"><circle cx="6" cy="6" r="5" fill="none" stroke="var(--amber)" stroke-width="1"/><ellipse cx="6" cy="6" rx="2.2" ry="5" fill="none" stroke="var(--amber)" stroke-width="0.9"/><path d="M1 6 H11 M2 3.5 H10 M2 8.5 H10" stroke="var(--amber)" stroke-width="0.8"/></svg>
          Stonefieldcustombuilders-example.com
        </li>
      </ul>
    </div>
  </section>

  <section class="card card-back">
    <div class="brand">
      <span class="brand-mark"></span>
      <p class="brand-name">Stonefield<br>Custom Builders</p>
    </div>
  </section>
</body>
</html>
```